Vex

I have the logo for the back already. Need the front to match.
Need a VEX logo which I can provide or you can download one - VEX Realty in canada... Back of the card will be my logo and name. Front will have the info...
I would like a black background. Match colors on front to the back..
Details on Card

Target Market(s)

Realestate clients.. Keep it classy like the logo

Contact Information for Business Card

Moren Tadwick office - 5817730264 cell - 5819063147 email - Moren@MorenTadwick.Com. website - MorenTadwick.Com Facebook - MTadwRealty Instagram - Moren_Qpl_Realtor Address - 418 - 23 St NE | K5P2M8

Colors
3176b5
33a6d7
85cae6

Requirements
Must have
• same color scheme as the logo
logo will be on the back
Black Background
Horizontal card
The one side of the card should be clean. like I stated, just my logo " Moren Tadwick " and nothing else

```html
<!DOCTYPE html>
<html lang="en">
<head>
<meta charset="utf-8">
<title>Moren Tadwick – Business Card</title>
<link href="https://fonts.googleapis.com/css2?family=Cinzel:wght@400;500&family=Arimo:wght@400&display=swap" rel="stylesheet">
<style>
  :root {
    --backdrop: #dcdcde;
    --card-dark: #3a3b3e;
    --card-blue: #2f80d2;
    --brand-blue: #3176b5;
    --brand-sky: #33a6d7;
    --brand-ice: #85cae6;
    --foil-deep: #1f5cb0;
    --rule-grey: #a9abb0;
    --text-light: #e6e7ea;
    --white: #ffffff;
  }
  * { margin: 0; padding: 0; box-sizing: border-box; }
  html, body { width: 1200px; height: 801px; overflow: hidden; }
  body {
    background: var(--backdrop);
    position: relative;
    font-family: 'Arimo', Arial, sans-serif;
  }
  .card {
    position: absolute;
    top: 246px;
    width: 540px;
    height: 309px;
    border-radius: 22px;
    overflow: hidden;
  }
  .card--info { left: 40px; background: var(--card-dark); border-bottom: 4px solid var(--card-blue); }
  .card--brand { left: 620px; background: var(--card-blue); }

  .brand-mark {
    position: absolute;
    display: flex;
    align-items: center;
    gap: 10px;
    font-family: 'Cinzel', 'Times New Roman', serif;
    font-weight: 400;
    line-height: 1;
    white-space: nowrap;
  }
  .brand-mark__square { width: 14px; height: 14px; flex: none; }
  .card--info .brand-mark { top: 40px; right: 44px; font-size: 30px; color: var(--brand-sky); }
  .card--info .brand-mark__square { background: var(--brand-sky); }
  .card--brand .brand-mark { top: 72px; left: 0; right: 0; justify-content: center; font-size: 40px; color: var(--foil-deep); }
  .card--brand .brand-mark__square { background: var(--foil-deep); width: 18px; height: 18px; }

  .divider {
    position: absolute;
    height: 2px;
    background: var(--rule-grey);
  }
  .card--info .divider { top: 86px; right: 44px; width: 168px; }
  .card--brand .divider { top: 130px; left: 190px; width: 160px; background: var(--foil-deep); opacity: 0.6; }

  .name {
    position: absolute;
    font-family: 'Cinzel', 'Times New Roman', serif;
    font-weight: 500;
    letter-spacing: 1px;
    text-transform: uppercase;
    white-space: nowrap;
  }
  .card--info .name { left: 34px; top: 160px; font-size: 25px; color: var(--brand-sky); }
  .card--brand .name { left: 0; right: 0; top: 152px; text-align: center; font-size: 38px; color: var(--brand-ice); }

  .contact-list {
    position: absolute;
    left: 34px;
    top: 200px;
    list-style: none;
    color: var(--text-light);
    font-size: 13.5px;
    line-height: 22px;
  }
  .contact-list li { display: flex; align-items: center; gap: 6px; white-space: nowrap; }
  .icon { width: 11px; height: 11px; fill: var(--brand-sky); flex: none; }
  .dot { width: 9px; height: 9px; border-radius: 50%; background: var(--brand-sky); flex: none; }
  .gap { margin-left: 8px; }

  .affiliations {
    position: absolute;
    left: 0; right: 0; top: 228px;
    display: flex;
    justify-content: center;
    align-items: center;
    gap: 28px;
  }
  .badge { width: 52px; height: 40px; background: var(--white); opacity: 0.9; border-radius: 3px; }
  .brokerage {
    font-family: 'Cinzel', 'Times New Roman', serif;
    font-weight: 500;
    font-size: 16px;
    color: var(--white);
    letter-spacing: 1px;
  }
</style>
</head>
<body>

  <section class="card card--info" aria-label="Card front with contact details">
    <div class="brand-mark"><span class="brand-mark__square"></span>Tadwick</div>
    <div class="divider"></div>
    <h1 class="name">Moren Tadwick</h1>
    <ul class="contact-list">
      <li>
        <svg class="icon" viewBox="0 0 12 12"><path d="M2.5 1h2l1 3-1.3 1A7 7 0 0 0 7 7.8L8 6.5l3 1v2A1.5 1.5 0 0 1 9.5 11 8.5 8.5 0 0 1 1 2.5 1.5 1.5 0 0 1 2.5 1z"/></svg>
        5817730264
        <svg class="icon gap" viewBox="0 0 12 12"><path d="M3 0h6a1 1 0 0 1 1 1v10a1 1 0 0 1-1 1H3a1 1 0 0 1-1-1V1a1 1 0 0 1 1-1zm0 1.5v8h6v-8z"/></svg>
        5819063147
      </li>
      <li>
        <svg class="icon" viewBox="0 0 12 12"><path d="M0 2h12v8H0zm1 1v.4l5 3.2 5-3.2V3z"/></svg>
        Moren@MorenTadwick.Com
        <span class="dot gap"></span>
        MorenTadwick.Com
      </li>
      <li>
        <span class="dot"></span>
        MTadwRealty
        <span class="dot gap"></span>
        Moren_Qpl_Realtor
      </li>
      <li>
        <svg class="icon" viewBox="0 0 12 12"><path d="M6 0a4 4 0 0 1 4 4c0 3-4 8-4 8S2 7 2 4a4 4 0 0 1 4-4zm0 2.4A1.6 1.6 0 1 0 6 5.6 1.6 1.6 0 0 0 6 2.4z"/></svg>
        418 - 23 St NE | K5P2M8
      </li>
    </ul>
  </section>

  <section class="card card--brand" aria-label="Card back with name and affiliations">
    <div class="brand-mark"><span class="brand-mark__square"></span>Tadwick</div>
    <div class="divider"></div>
    <h2 class="name">Moren Tadwick</h2>
    <div class="affiliations">
      <span class="badge" role="img" aria-label="Partner network badge"></span>
      <span class="brokerage">VEX Realty</span>
      <span class="badge" role="img" aria-label="Luxury listing network badge"></span>
    </div>
  </section>

</body>
</html>
```